El Surco Movie poster

We need to design a 27"x40" movie poster for our documentary.
El Surco is a story of the American Dream seen through the eyes of modern day immigrants. Their journey takes them from their humble beginnings in Mexico, crossing the border to become day laborers in the fields of Napa, and to eventually owning their own vineyards and making their own wine. We need a movie poster that articulates the simple but difficult journey from the soil to a bottle of wine.

```html
<!DOCTYPE html>
<html lang="en">
<head>
<meta charset="utf-8">
<title>El Surco — Movie Poster</title>
<link rel="stylesheet" href="https://fonts.googleapis.com/css2?family=Figtree:wght@300;400&display=swap">
<style>
  :root {
    --backdrop: #1b1513;
    --soil-light: #c9a08c;
    --soil-mid: #9c705f;
    --soil-dark: #5a3a30;
    --night: #050303;
    --wine: #5c0d16;
    --title-top: #f4cdb8;
    --title-bottom: #d9977c;
    --copy: #f0c8b3;
  }
  * { margin: 0; padding: 0; box-sizing: border-box; }
  html, body {
    width: 1200px;
    height: 2569px;
    overflow: hidden;
    background: var(--backdrop);
  }
  .canvas {
    position: relative;
    width: 1200px;
    height: 2569px;
    display: flex;
    align-items: center;
    justify-content: center;
  }
  .poster {
    position: relative;
    width: 1200px;
    height: 1778px;
    overflow: hidden;
    background: var(--night);
  }
  .poster__photo {
    position: absolute;
    inset: 0;
    background:
      radial-gradient(ellipse 70% 14% at 50% 92%, rgba(140, 20, 35, 0.75), transparent 70%),
      linear-gradient(180deg,
        var(--soil-mid) 0%,
        var(--soil-light) 12%,
        #b88c78 28%,
        var(--soil-mid) 38%,
        #c49a86 52%,
        var(--soil-dark) 60%,
        #140b09 68%,
        var(--night) 80%,
        #0c0406 100%);
  }
  .poster__stream {
    position: absolute;
    left: 50%;
    top: 520px;
    width: 6px;
    height: 1100px;
    margin-left: 37px;
    background: linear-gradient(180deg, rgba(92, 13, 22, 0) 0%, var(--wine) 20%, var(--wine) 100%);
  }
  .poster__title {
    position: absolute;
    left: 0;
    right: 0;
    top: 560px;
    text-align: center;
    font-family: "Figtree", "Helvetica Neue", sans-serif;
    font-weight: 300;
    font-size: 300px;
    line-height: 0.9;
    letter-spacing: -0.02em;
    background: linear-gradient(180deg, var(--title-top), var(--title-bottom));
    -webkit-background-clip: text;
    background-clip: text;
    color: transparent;
  }
  .poster__title span { display: block; }
  .poster__synopsis {
    position: absolute;
    left: 50%;
    top: 1372px;
    width: 680px;
    transform: translateX(-50%);
    text-align: center;
    font-family: "Figtree", "Helvetica Neue", sans-serif;
    font-weight: 400;
    font-size: 21px;
    line-height: 1.22;
    color: var(--copy);
  }
</style>
</head>
<body>
  <div class="canvas">
    <article class="poster">
      <div class="poster__photo" role="img" aria-label="A hand pouring reddish soil that turns into a stream of red wine falling into a wine glass against a dark background"></div>
      <div class="poster__stream" aria-hidden="true"></div>
      <h1 class="poster__title"><span>EL</span><span>SURCO</span></h1>
      <p class="poster__synopsis">El Surco is a story of the American Dream seen through the eyes of modern day immigrants. Their journey takes them from their humble beginnings in Mexico, crossing the border to become day laborers in the fields of Napa, and to eventually owning their own vineyards and making their own wine.</p>
    </article>
  </div>
</body>
</html>
```